Criação de Papelaria (6 itens) para Brisa & Lajedo
" Prestamos serviços de outorga e licenças ambientais, análise de água, aproveitamento de águas, pesquisa de água mineral, poços artesianos (furação, recuperação, tratamento de água), energia solar, etc. "

```html
<!DOCTYPE html>
<html lang="pt-BR">
<head>
<meta charset="utf-8">
<title>Brisa &amp; Lajedo – Assinatura de e-mail</title>
<link href="https://fonts.googleapis.com/css2?family=Arimo:wght@400;700&display=swap" rel="stylesheet">
<style>
  :root {
    --backdrop: #b9babc;
    --paper: #ffffff;
    --brand-blue: #2f5e9d;
    --brand-green: #5f8a3a;
    --text-light: #ffffff;
  }
  * { margin: 0; padding: 0; box-sizing: border-box; }
  html, body {
    width: 1200px; height: 1200px; overflow: hidden;
    background: var(--backdrop);
    font-family: "Arimo", Arial, sans-serif;
  }
  .signature {
    position: absolute;
    left: 101px; top: 480px;
    width: 998px; height: 168px;
    background: var(--paper);
  }
  .signature__shape {
    position: absolute; inset: 0;
    width: 100%; height: 100%;
  }
  .brand {
    position: absolute;
    left: 78px; top: 58px;
    display: flex; align-items: center; gap: 14px;
  }
  .brand__dot {
    width: 22px; height: 22px; border-radius: 50%;
    background: var(--brand-green);
  }
  .brand__name {
    font-size: 38px; font-weight: 700;
    color: var(--brand-blue);
    letter-spacing: -0.5px;
  }
  .contact {
    position: absolute;
    right: 10px; top: 0; left: 470px; height: 100%;
    color: var(--text-light);
  }
  .contact__name {
    position: absolute;
    right: 30px; top: 20px;
    font-size: 25px; font-weight: 400;
    white-space: nowrap;
  }
  .contact__rule {
    position: absolute;
    left: 195px; right: -10px; top: 57px;
    height: 1px; background: rgba(255,255,255,0.7);
  }
  .contact__lines {
    position: absolute;
    right: 14px; top: 80px;
    text-align: right;
    font-size: 11.5px; line-height: 15px;
    white-space: nowrap;
  }
  .contact__address {
    position: absolute;
    right: 4px; top: 146px;
    font-size: 11.5px; line-height: 14px;
    white-space: nowrap;
  }
</style>
</head>
<body>
  <section class="signature" aria-label="Assinatura de e-mail Brisa &amp; Lajedo">
    <svg class="signature__shape" viewBox="0 0 998 168" preserveAspectRatio="none" aria-hidden="true">
      <path d="M458,0 Q424,84 458,168" fill="none" stroke="var(--brand-green)" stroke-width="3"/>
      <path d="M472,0 Q438,84 472,168 L998,168 L998,0 Z" fill="var(--brand-blue)"/>
    </svg>

    <div class="brand">
      <span class="brand__dot"></span>
      <span class="brand__name">Brisa &amp; Lajedo</span>
    </div>

    <div class="contact">
      <p class="contact__name">Nome/Sobre Nome</p>
      <span class="contact__rule"></span>
      <p class="contact__lines">
        (00) 00000-0000<br>
        (00) 0000-0000<br>
        www.brisaelajedo.com.br<br>
        contato@brisaelajedo.com.br
      </p>
      <p class="contact__address">Rua das Palmeiras nº120 - Centro - São Paulo - SP - 01000-000</p>
    </div>
  </section>
</body>
</html>
```